Navelo Partnering Business Card

Hello everyone. We need a business card design that would match our logo and the theme we're trying to have for Navelo that you can find on our website and/or Corvapage page

```html
<!DOCTYPE html>
<html lang="en">
<head>
<meta charset="utf-8">
<title>Navelo Partnering Business Card</title>
<link rel="stylesheet" href="https://fonts.googleapis.com/css2?family=Open+Sans:wght@400;600;700&display=swap">
<style>
  :root {
    --page: #ffffff;
    --frame: #c9c9c9;
    --blue-deep: #0b0585;
    --blue-mid: #1508c9;
    --blue-bright: #2a1ef0;
    --blue-glow: #5a4cff;
    --paper: #fbfcfa;
    --paper-shade: #f1f4f5;
    --ink: #170c86;
    --white: #ffffff;
  }
  * { margin: 0; padding: 0; box-sizing: border-box; }
  html, body { width: 1200px; height: 1200px; overflow: hidden; background: var(--page); }
  body { font-family: "Open Sans", sans-serif; position: relative; }
  .canvas {
    position: absolute; inset: 0;
    border: 2px solid var(--frame);
  }
  .card {
    position: absolute; left: 209px; width: 782px; height: 489px;
    overflow: hidden;
    background: linear-gradient(135deg, var(--blue-mid) 0%, var(--blue-deep) 100%);
    outline: 1px solid #d8d8e8;
  }
  .card--front { top: 94px; }
  .card--back { top: 618px; }
  .card svg { position: absolute; inset: 0; }
  .brand-name {
    position: absolute; font-weight: 700; letter-spacing: -1px; line-height: 1;
  }
  .card--front .brand-name { left: 88px; top: 152px; font-size: 66px; color: var(--ink); }
  .card--back .brand-name { left: 0; right: 0; text-align: center; top: 203px; font-size: 70px; color: var(--white); }
  .holder-name {
    position: absolute; left: 455px; top: 72px;
    font-size: 40px; font-weight: 600; color: var(--white); line-height: 1;
  }
  .contact { position: absolute; color: var(--white); }
  .contact svg { position: absolute; left: -18px; top: 2px; width: 13px; height: 13px; }
  .contact__label { font-size: 12.5px; font-weight: 600; line-height: 16px; }
  .contact__value { font-size: 11px; line-height: 14px; white-space: nowrap; }
  .contact--address { left: 473px; top: 337px; }
  .contact--mobile { left: 653px; top: 337px; }
  .contact--email { left: 473px; top: 395px; }
  .contact--web { left: 653px; top: 395px; }
  .back-url {
    position: absolute; right: 25px; top: 448px;
    font-size: 14px; color: var(--white); letter-spacing: 0.3px;
  }
</style>
</head>
<body>
<div class="canvas">

  <section class="card card--front">
    <svg viewBox="0 0 782 489" width="782" height="489" aria-hidden="true">
      <path d="M239 0 C340 40 400 110 395 220 C388 340 250 440 120 489 L150 489 C300 430 415 330 420 210 C424 110 370 40 300 0 Z" fill="var(--blue-glow)" opacity="0.35"/>
      <path d="M239 0 C330 45 385 120 380 215 C372 340 250 440 110 489 L130 489 C280 430 395 330 400 210 C404 110 350 40 275 0 Z" fill="var(--blue-bright)" opacity="0.6"/>
      <path d="M0 0 L239 0 C330 45 378 120 375 200 C368 330 240 440 117 489 L0 489 Z" fill="var(--paper-shade)"/>
      <path d="M0 0 L239 0 C330 45 378 120 375 200 C372 270 350 300 330 330 C260 390 130 400 0 335 Z" fill="var(--paper)"/>
      <g stroke="var(--blue-glow)" stroke-width="0.6" fill="none" opacity="0.4">
        <path d="M420 489 C560 440 680 430 782 420"/>
        <path d="M460 489 C590 450 700 440 782 430"/>
        <path d="M500 489 C620 455 710 445 782 440"/>
      </g>
    </svg>
    <div class="brand-name">Navelo</div>

    <div class="holder-name">John Doe</div>

    <div class="contact contact--address">
      <svg viewBox="0 0 12 16"><path d="M6 0a5 5 0 0 1 5 5c0 4-5 11-5 11S1 9 1 5a5 5 0 0 1 5-5zm0 3a2 2 0 1 0 0 4 2 2 0 0 0 0-4z" fill="#fff"/></svg>
      <div class="contact__label">ADDRESS</div>
      <div class="contact__value">2471 Elm Grove<br>Lane, GT 40318</div>
    </div>
    <div class="contact contact--mobile">
      <svg viewBox="0 0 10 16"><rect x="1" y="0.8" width="8" height="14.4" rx="1.5" fill="none" stroke="#fff" stroke-width="1.4"/><circle cx="5" cy="12.5" r="0.9" fill="#fff"/></svg>
      <div class="contact__label">Mobile</div>
      <div class="contact__value">045 - 782 - 1930</div>
    </div>
    <div class="contact contact--email">
      <svg viewBox="0 0 16 12"><rect x="0.7" y="0.7" width="14.6" height="10.6" fill="none" stroke="#fff" stroke-width="1.4"/><path d="M1 1l7 6 7-6" fill="none" stroke="#fff" stroke-width="1.4"/></svg>
      <div class="contact__label">E-mail</div>
      <div class="contact__value">hello@navelo.com</div>
    </div>
    <div class="contact contact--web">
      <svg viewBox="0 0 16 16"><g fill="none" stroke="#fff" stroke-width="1.2"><circle cx="8" cy="8" r="7"/><ellipse cx="8" cy="8" rx="3" ry="7"/><path d="M1 8h14M2.5 4h11M2.5 12h11"/></g></svg>
      <div class="contact__label">Website</div>
      <div class="contact__value">www.navelo.com</div>
    </div>
  </section>

  <section class="card card--back">
    <svg viewBox="0 0 782 489" width="782" height="489" aria-hidden="true">
      <path d="M10 240 C90 110 230 10 420 0 L300 0 C170 30 70 120 10 240 Z" fill="var(--blue-glow)" opacity="0.35"/>
      <path d="M60 150 C140 70 230 25 350 0 L260 0 C170 30 100 80 60 150 Z" fill="var(--blue-bright)" opacity="0.55"/>
      <path d="M560 489 C660 440 740 390 782 330 L782 360 C740 420 680 460 610 489 Z" fill="var(--blue-glow)" opacity="0.5"/>
      <path d="M540 489 C640 450 730 400 782 350 L782 280 C740 370 650 440 520 489 Z" fill="var(--blue-bright)" opacity="0.3"/>
      <g stroke="var(--blue-glow)" stroke-width="0.6" fill="none" opacity="0.35">
        <path d="M0 130 C250 125 520 130 782 110"/>
        <path d="M0 135 C260 132 520 140 782 125"/>
      </g>
    </svg>
    <div class="brand-name">Navelo</div>
    <div class="back-url">www.navelo.com</div>
  </section>

</div>
</body>
</html>
```